Harbourline Strategy Group firm

I need a business card that is succint for a Brisbane based business called Harbourline Strategy Group Pty Ltd.
We bridge the gaps between People, Process and Technology.

We are a specialist operational excellence firm, delivering strategic consulting and business advisory services in six core capabilities, across all industries and all business lines to improve performance, efficiency, profitability, automation and scalability, for clients across Australia &New Zealand.
Updates

Hi Designers, I have uploaded the logo in 3D .png format, to assist in card design.

Target Market(s)

Project Management professionals, IT professionals, corporate and government clients managing transitioning or transformation projects.

Contact Information for Business Card

Harbourline Strategy Group Pty Ltd

Daniel Ferreira
Principal Consultant

mobile: +61 417 260 315
email: daniel@harbourlinestrategygroup.com.au
webpage: www.harbourlinestrategygroup.com

professional services: strategic advisors,

Font styles to use
Sans Serif

Requirements
Must have
• Business name: Harbourline Strategy Group
logo: attached
Contact person: Daniel Ferreira
Title: Principal Consultant
contact details:
mobile +61 417 260
email: daniel@HarbourlineStrategyGroup.com.au
website: HarbourlineStrategyGroup.com

on back side with logo include: A.B.N. 58210947362

professional services offered: Business Analysis, Strategic Advisory
Nice to have
• QR code
Should not have
• contacts picture

```html
<!DOCTYPE html>
<html lang="en">
<head>
<meta charset="utf-8">
<title>Harbourline Strategy Group – Business Card</title>
<link rel="stylesheet" href="https://fonts.googleapis.com/css2?family=Oswald:wght@600&family=Roboto:wght@400;700;900&display=swap">
<style>
  :root {
    --page-bg: #f1eeee;
    --card-front: #2b2a2b;
    --card-back: #262526;
    --pattern-tone: #333233;
    --brand-red: #e8343f;
    --ink-white: #ffffff;
    --ink-dark: #1d1d24;
    --pill-light: #f4f4f4;
    --pill-mid: #b9b9bb;
    --icon-deep: #5a1c20;
  }
  * { margin: 0; padding: 0; box-sizing: border-box; }
  html, body { width: 1200px; height: 1200px; overflow: hidden; }
  body {
    background: var(--page-bg);
    position: relative;
    font-family: "Roboto", Arial, sans-serif;
  }
  .card {
    position: absolute;
    left: 250px;
    width: 700px;
    height: 400px;
    border-radius: 20px;
    overflow: hidden;
  }
  .card--front { top: 178px; background: var(--card-front); }
  .card--back { top: 622px; background: var(--card-back); }

  .front-pattern {
    position: absolute;
    inset: 0;
    background: var(--pattern-tone);
    opacity: 0.55;
  }
  .front-brand {
    position: absolute;
    left: 0; right: 0;
    top: 152px;
    display: flex;
    align-items: center;
    justify-content: center;
    gap: 16px;
  }
  .brand-square {
    width: 58px; height: 58px;
    background: var(--brand-red);
  }
  .brand-name {
    font-family: "Roboto", Arial, sans-serif;
    font-weight: 900;
    color: var(--brand-red);
    text-transform: uppercase;
    line-height: 0.95;
  }
  .front-brand .brand-name { font-size: 34px; }
  .abn {
    position: absolute;
    left: 436px;
    top: 244px;
    font-size: 10px;
    font-weight: 700;
    color: var(--ink-white);
    letter-spacing: 0.4px;
  }

  .back-brand {
    position: absolute;
    left: 20px;
    top: 162px;
    display: flex;
    align-items: center;
    gap: 10px;
  }
  .back-brand .brand-square { width: 32px; height: 32px; }
  .back-brand .brand-name { font-size: 19px; }

  .person {
    position: absolute;
    left: 230px;
    width: 400px;
    top: 32px;
    text-align: center;
  }
  .person-name {
    font-family: "Oswald", "Arial Narrow", sans-serif;
    font-weight: 600;
    font-size: 20px;
    letter-spacing: 1.2px;
    color: var(--ink-white);
    text-transform: uppercase;
  }
  .person-title {
    margin-top: 2px;
    font-size: 15px;
    color: var(--brand-red);
  }

  .contact {
    position: absolute;
    left: 270px;
    display: flex;
    align-items: center;
    gap: 9px;
  }
  .contact--phone { top: 207px; }
  .contact--email { top: 251px; }
  .contact--web { top: 301px; }
  .contact-icon { width: 30px; height: 30px; flex: none; }
  .contact-pill {
    position: relative;
    height: 26px;
    display: flex;
    align-items: center;
    padding: 0 14px;
  }
  .contact-pill svg {
    position: absolute;
    inset: 0;
    width: 100%;
    height: 100%;
  }
  .contact-text {
    position: relative;
    font-size: 16px;
    color: var(--ink-dark);
    white-space: nowrap;
  }
</style>
</head>
<body>

<section class="card card--front" aria-label="Card front">
  <div class="front-pattern" role="img" aria-label="Subtle repeating pattern of small upward arrows"></div>
  <div class="front-brand">
    <span class="brand-square"></span>
    <span class="brand-name">Harbourline<br>Strategy Group</span>
  </div>
  <p class="abn">A.B.N. 58210947362</p>
</section>

<section class="card card--back" aria-label="Card back">
  <div class="back-brand">
    <span class="brand-square"></span>
    <span class="brand-name">Harbourline<br>Strategy Group</span>
  </div>

  <div class="person">
    <p class="person-name">Daniel Ferreira</p>
    <p class="person-title">Principal Consultant</p>
  </div>

  <svg width="0" height="0" style="position:absolute">
    <defs>
      <linearGradient id="pillFill" x1="0" y1="0" x2="1" y2="0">
        <stop offset="0" stop-color="#f6f6f6"/>
        <stop offset="1" stop-color="#aeaeb1"/>
      </linearGradient>
      <radialGradient id="iconFill" cx="0.5" cy="0.4" r="0.6">
        <stop offset="0" stop-color="#8c2a30"/>
        <stop offset="1" stop-color="#3d1215"/>
      </radialGradient>
    </defs>
  </svg>

  <div class="contact contact--phone">
    <svg class="contact-icon" viewBox="0 0 30 30" aria-hidden="true">
      <circle cx="15" cy="15" r="14" fill="#4a4a4c"/>
      <circle cx="15" cy="15" r="11" fill="url(#iconFill)"/>
      <path d="M11 9.5l2.2-.6 1.3 3-1.3 1a7 7 0 0 0 3.4 3.4l1-1.3 3 1.3-.6 2.2c-5.5.3-9.3-3.5-9-9z" fill="#1a1a1a"/>
    </svg>
    <div class="contact-pill" style="width:160px">
      <svg viewBox="0 0 160 26" preserveAspectRatio="none" aria-hidden="true">
        <polygon points="7,1 151,1 159,13 151,25 7,25 1,13" fill="url(#pillFill)" stroke="#e8343f" stroke-width="1.5"/>
      </svg>
      <span class="contact-text">+61 417 260 315</span>
    </div>
  </div>

  <div class="contact contact--email">
    <svg class="contact-icon" viewBox="0 0 30 30" aria-hidden="true">
      <circle cx="15" cy="15" r="14" fill="#4a4a4c"/>
      <circle cx="15" cy="15" r="11" fill="url(#iconFill)"/>
      <rect x="10" y="11.5" width="10" height="7" fill="#1a1a1a"/>
      <path d="M10 11.5l5 4 5-4" fill="none" stroke="#8c2a30" stroke-width="1"/>
    </svg>
    <div class="contact-pill" style="width:357px">
      <svg viewBox="0 0 357 26" preserveAspectRatio="none" aria-hidden="true">
        <polygon points="7,1 348,1 356,13 348,25 7,25 1,13" fill="url(#pillFill)" stroke="#e8343f" stroke-width="1.5"/>
      </svg>
      <span class="contact-text">daniel@harbourlinestrategygroup.com.au</span>
    </div>
  </div>

  <div class="contact contact--web">
    <svg class="contact-icon" viewBox="0 0 30 30" aria-hidden="true">
      <circle cx="15" cy="15" r="14" fill="#4a4a4c"/>
      <circle cx="15" cy="15" r="11" fill="url(#iconFill)"/>
      <g fill="none" stroke="#1a1a1a" stroke-width="1.2">
        <circle cx="15" cy="15" r="5.5"/>
        <ellipse cx="15" cy="15" rx="2.4" ry="5.5"/>
        <line x1="9.5" y1="15" x2="20.5" y2="15"/>
      </g>
    </svg>
    <div class="contact-pill" style="width:341px">
      <svg viewBox="0 0 341 26" preserveAspectRatio="none" aria-hidden="true">
        <polygon points="7,1 332,1 340,13 332,25 7,25 1,13" fill="url(#pillFill)" stroke="#e8343f" stroke-width="1.5"/>
      </svg>
      <span class="contact-text">Web www.harbourlinestrategygroup.com</span>
    </div>
  </div>
</section>

</body>
</html>
```